Kesta furniture

A single page e commerce website for a new furniture company.

The opening range would consist of 3 collections - Each collection would consist of a bed , sofa & arm chair.

So total 9 items.

We would want a single page which has the 3 collections on it which are available to purchase from the website.

See attached the logo & branding for colours

Target Market(s)

customers wanting to buy high end furniture

Industry/Entity Type

furniture retail

Coding

Coded - Design and coding required

Number of Pages Required

1 page

Colors
00AB8E
00BBA5
67D7C9
C6EFE9
E9F9F6

```html
<!DOCTYPE html>
<html lang="en">
<head>
<meta charset="UTF-8">
<title>Kesta Furniture</title>
<link rel="stylesheet" href="https://fonts.googleapis.com/css2?family=Poppins:wght@400;500&display=swap">
<style>
:root{
  --teal:#00a8b4;
  --ink:#151515;
  --text:#333;
  --muted:#8a8a8a;
  --hero:#e6e6e6;
  --band:#f2f2f2;
  --soft:#f5f4f5;
  --tab:#e4e4e4;
  --dark:#2b2b2b;
  --foot:#e0e0e0;
  --white:#fff;
}
*{margin:0;padding:0;box-sizing:border-box}
html,body{width:740px;height:1200px;overflow:hidden}
body{position:relative;background:var(--white);font-family:'Poppins',sans-serif;color:var(--text)}
.abs{position:absolute}
.header{left:0;top:0;width:740px;height:61px;background:var(--white)}
.brand{left:53px;top:0;width:89px;height:116px;background:var(--white);z-index:2;display:flex;flex-direction:column;align-items:center;justify-content:center;gap:6px}
.brand-mark{width:22px;height:22px;background:var(--teal)}
.brand-name{color:var(--teal);font-size:10px;font-weight:500;text-align:center;line-height:1.2}
.nav a{position:absolute;top:37px;font-size:10px;color:var(--text);text-decoration:none}
.nav .active{color:var(--teal)}
.nav-dot{left:360px;top:58px;width:14px;height:10px;border-radius:0 0 7px 7px;background:var(--white);z-index:2}
.hero{left:0;top:61px;width:740px;height:319px;background:radial-gradient(ellipse at 75% 40%,#f0f0f0,var(--hero) 70%)}
.hero-title{left:53px;top:138px;font-size:39px;font-weight:500;color:var(--ink);letter-spacing:-.3px}
.hero-text{left:56px;top:187px;width:360px;font-size:8.4px;line-height:12.7px}
.btn{background:var(--teal);color:var(--white);display:flex;align-items:center;justify-content:center;font-weight:500}
.hero-btn{left:53px;top:232px;width:107px;height:28px;font-size:9px}
.hero-photo{left:188px;top:219px;width:492px;height:161px;background:linear-gradient(180deg,#3a2f2e,#1b1515);border-radius:18px 18px 4px 4px}
.features{left:0;top:380px;width:740px;height:166px;background:var(--band)}
.feature{top:405px;width:202px;height:116px;background:var(--white);box-shadow:0 0 2px rgba(0,0,0,.08);text-align:center}
.feature-icon{position:absolute;left:83px;top:13px;width:36px;height:34px;background:var(--teal);display:flex;align-items:center;justify-content:center}
.feature h3{position:absolute;top:54px;width:100%;font-size:8.6px;font-weight:500;color:var(--text);letter-spacing:.3px}
.feature p{position:absolute;top:70px;left:10px;right:10px;font-size:8px;line-height:12.7px;color:var(--muted)}
.section-title{left:55px;top:587px;font-size:25px;font-weight:500;color:var(--ink)}
.tab{top:639px;width:147px;height:34px;background:var(--tab);font-size:9.5px;color:var(--ink);display:flex;align-items:center;justify-content:center}
.tab.active{background:var(--soft)}
.collection{left:0;top:673px;width:740px;height:304px;background:var(--soft)}
.product{top:714px;width:186px;height:209px;background:var(--white);border:1px solid #ececec;text-align:center}
.product-photo{position:absolute;left:5px;top:5px;width:176px;height:120px}
.product h4{position:absolute;top:134px;width:100%;font-size:10.5px;font-weight:400;color:var(--ink)}
.price{position:absolute;top:152px;width:100%;font-size:8px;color:var(--ink)}
.price s{color:var(--muted)}
.product .btn{position:absolute;left:54px;top:178px;width:77px;height:19px;font-size:7.5px}
.footer{left:0;top:977px;width:740px;height:174px;background:var(--teal);color:var(--white)}
.foot-brand{left:53px;top:1013px;width:73px;height:80px;border:2px solid var(--white);border-radius:3px;display:flex;flex-direction:column;align-items:center;justify-content:center;gap:6px}
.foot-brand .brand-mark{background:var(--white);width:16px;height:16px}
.foot-brand .brand-name{color:var(--white);font-size:8.5px}
.foot-h{font-size:11.5px;font-weight:500;color:var(--white)}
.foot-text{left:136px;top:1032px;width:185px;font-size:8.3px;line-height:12.7px;color:var(--white)}
.links{left:351px;top:1032px;list-style:none;font-size:8.3px;line-height:15.9px}
.links li::before{content:"›";margin-right:5px}
.news-text{left:459px;top:1032px;font-size:9.5px}
.input{left:460px;top:1058px;width:213px;height:23px;background:#e3e3e3;color:#888;font-size:8.3px;padding-left:8px;display:flex;align-items:center}
.sub-btn{left:460px;top:1090px;width:84px;height:24px;background:var(--dark);color:var(--white);font-size:8.5px;display:flex;align-items:center;justify-content:center}
.bottom{left:0;top:1151px;width:740px;height:49px;background:var(--foot);font-size:8.3px;display:flex;align-items:center;justify-content:center;color:var(--text)}
</style>
</head>
<body>
<header class="abs header"></header>
<div class="abs brand"><span class="brand-mark"></span><span class="brand-name">Kesta furniture</span></div>
<nav class="nav">
  <a class="active" style="left:354px">Home</a>
  <a style="left:409px">About Us</a>
  <a style="left:481px">Our Products</a>
  <a style="left:570px">Contact</a>
</nav>
<svg class="abs" style="left:645px;top:38px" width="13" height="13" viewBox="0 0 13 13" fill="none" stroke="#333" stroke-width="1.4"><circle cx="5.5" cy="5.5" r="4.3"/><path d="M8.7 8.7l3.3 3.3"/></svg>
<svg class="abs" style="left:667px;top:32px" width="24" height="20" viewBox="0 0 24 20"><path d="M1 6h3l2.5 8h8.5l2-6H6" fill="none" stroke="#333" stroke-width="1.5"/><path d="M5 7h12.5l-2 6.5H7z" fill="#333"/><circle cx="8" cy="16.5" r="1.4" fill="#333"/><circle cx="14" cy="16.5" r="1.4" fill="#333"/><circle cx="18" cy="6" r="5.2" fill="#00a8b4"/><text x="18" y="8" font-size="6" fill="#fff" text-anchor="middle" font-family="Poppins,sans-serif">2</text></svg>

<section class="abs hero"></section>
<div class="abs nav-dot"></div>
<h1 class="abs hero-title">Modern Furniture</h1>
<p class="abs hero-text">Lorem Ipsum is simply dummy text of the printing and typesetting industry. Lorem Ipsum has been the industry's standard dummy text ever since the 1500s.</p>
<div class="abs btn hero-btn">SHOP NOW</div>
<div class="abs hero-photo" role="img" aria-label="Two black leather reclining sofas"></div>

<section class="abs features"></section>
<div class="abs feature" style="left:53px">
  <div class="feature-icon"><svg width="22" height="14" viewBox="0 0 22 14" fill="#fff"><rect x="4" y="1" width="10" height="9" rx="1"/><path d="M14 4h4l3 3v3h-7z"/><circle cx="8" cy="11.5" r="2" stroke="#00a8b4"/><circle cx="17" cy="11.5" r="2" stroke="#00a8b4"/><rect x="0" y="3" width="3" height="1"/><rect x="1" y="6" width="2" height="1"/></svg></div>
  <h3>WORLDWIDE DELIVERY</h3>
  <p>Lorem Ipsum has been the industry's standard dummy text ever</p>
</div>
<div class="abs feature" style="left:270px">
  <div class="feature-icon"><svg width="14" height="18" viewBox="0 0 14 18" fill="#fff"><path d="M4 1h6l-2 4h-2z"/><path d="M5 6h4c3 2 5 5 5 8 0 3-2 4-7 4s-7-1-7-4c0-3 2-6 5-8z"/><text x="7" y="15.5" font-size="7" fill="#00a8b4" text-anchor="middle" font-family="Poppins,sans-serif">$</text></svg></div>
  <h3>SECURE PAYMENTS</h3>
  <p>Lorem Ipsum has been the industry's standard dummy text ever</p>
</div>
<div class="abs feature" style="left:487px">
  <div class="feature-icon"><svg width="20" height="20" viewBox="0 0 20 20" fill="none" stroke="#fff" stroke-width="2.4"><path d="M3.5 9a6.5 6.5 0 0 1 11.5-3.5"/><path d="M16.5 11a6.5 6.5 0 0 1-11.5 3.5"/><path d="M15.5 1.5v4.5h-4.5" stroke-width="2"/><path d="M4.5 18.5v-4.5h4.5" stroke-width="2"/></svg></div>
  <h3>SIMPLE RETURNS</h3>
  <p>Lorem Ipsum has been the industry's standard dummy text ever</p>
</div>

<h2 class="abs section-title">Our Collections</h2>
<section class="abs collection"></section>
<div class="abs tab active" style="left:53px">Collections 1</div>
<div class="abs tab" style="left:203px">Collections 2</div>
<div class="abs tab" style="left:353px">Collections 3</div>

<div class="abs product" style="left:80px">
  <div class="product-photo" role="img" aria-label="Double bed with white linen in a bedroom" style="background:linear-gradient(180deg,#d9cfc4,#b7a699 60%,#8a6a5a)"></div>
  <h4>Product Bed</h4>
  <div class="price">$125 - <s>$160</s></div>
  <div class="btn">SHOP NOW</div>
</div>
<div class="abs product" style="left:281px">
  <div class="product-photo" role="img" aria-label="Grey sofa with cushions and a glass coffee table" style="background:linear-gradient(180deg,#e3e3e3,#8d8d8d 60%,#c9c9c9)"></div>
  <h4>Product Sofa</h4>
  <div class="price">$125 - <s>$160</s></div>
  <div class="btn">SHOP NOW</div>
</div>
<div class="abs product" style="left:483px">
  <div class="product-photo" role="img" aria-label="Red velvet arm chairs around a small tea table" style="background:linear-gradient(180deg,#7a5a40,#6a1a24 55%,#3a2a20)"></div>
  <h4>Product Arm Chair</h4>
  <div class="price">$125 - <s>$160</s></div>
  <div class="btn">SHOP NOW</div>
</div>

<footer class="abs footer"></footer>
<div class="abs foot-brand"><span class="brand-mark"></span><span class="brand-name">Kesta furniture</span></div>
<h5 class="abs foot-h" style="left:135px;top:1011px">About Us</h5>
<p class="abs foot-text">Lorem Ipsum is simply dummy text of the printing and typesetting industry. Lorem Ipsum has been the industry's standard dummy content</p>
<h5 class="abs foot-h" style="left:350px;top:1011px">Quick Links</h5>
<ul class="abs links" style="color:#fff">
  <li>About Us</li><li>Products</li><li>Collections</li><li>Support</li><li>Contact</li>
</ul>
<h5 class="abs foot-h" style="left:459px;top:1011px;font-size:13.5px">Subscribe Newsletter</h5>
<p class="abs news-text" style="color:#fff">Subscribe newsletter to get 5% on all products.</p>
<div class="abs input">Enter your email</div>
<div class="abs sub-btn">Subscribe</div>
<div class="abs bottom">Copyright ©2023 All rights reserved Kesta Furniture</div>
</body>
</html>
```